New Business Card Design Project

We require a business card design for Pharvelix, a newly established Indian company.
Our focus is on the development, manufacturing, and export of a diverse array of pharmaceutical products on a global scale. The card should convey a professional appearance, as our primary markets are in Africa, China, and Southeast Asian nations.
We envision a two-sided business card, with the reverse side dedicated to a logo set against a solid color or an elegantly designed pattern. The corners should be rounded. We would appreciate seeing both horizontal and vertical design options. We trust the designer to utilize their expertise in creating this design.

The content for the business card is included in the attached Word file.

Target Market(s)

Our primary markets are in Africa, China, and Southeast Asian, Latin America, Maldives, Sri Lanka

Industry/Entity Type

Pharmaceutical Manufacturing and Export

Contact Information for Business Card

Colors

Designer to choose colors to be used in the design.

Requirements
Must have
• The reverse side of the business card features solely the logo along with the tagline, "Care Beyond Borders."
Should not have
• The logo should not exceed two instances, encompassing both the front and back sides of the card.

```html
<!DOCTYPE html>
<html lang="en">
<head>
<meta charset="utf-8">
<title>Pharvelix Business Card</title>
<link href="https://fonts.googleapis.com/css2?family=Arimo:wght@400;700&display=swap" rel="stylesheet">
<style>
  :root {
    --backdrop: #3a3a3a;
    --brand-blue: #29a9e1;
    --deep-blue: #1a8fcf;
    --accent-red: #f15a4a;
    --paper: #ffffff;
    --ink-light: #ffffff;
  }
  * { box-sizing: border-box; margin: 0; padding: 0; }
  html, body {
    width: 1200px; height: 689px; overflow: hidden;
    background: var(--backdrop);
    font-family: "Arimo", Arial, sans-serif;
  }
  .stage { position: relative; width: 1200px; height: 689px; }
  .card {
    position: absolute; top: 201px;
    width: 500px; height: 286px;
    border-radius: 18px; overflow: hidden;
  }
  .card-back { left: 70px; background: var(--brand-blue); }
  .card-front { left: 630px; background: var(--paper); }

  .brand-lockup {
    position: absolute; left: 0; right: 0; top: 100px;
    display: flex; align-items: center; justify-content: center; gap: 12px;
  }
  .brand-mark { width: 22px; height: 22px; border-radius: 50%; flex: none; }
  .brand-name { font-weight: 700; font-size: 44px; letter-spacing: 0.5px; white-space: nowrap; }
  .card-back .brand-mark { background: var(--deep-blue); }
  .card-back .brand-name { color: var(--deep-blue); }
  .tagline {
    position: absolute; left: 0; right: 0; top: 170px;
    text-align: center; color: var(--ink-light); font-size: 14px;
  }

  .front-panel { position: absolute; inset: 0; }
  .card-front .brand-lockup { left: 30px; right: 200px; top: 118px; gap: 10px; }
  .card-front .brand-mark { background: var(--brand-blue); width: 18px; height: 18px; }
  .card-front .brand-name { color: var(--brand-blue); font-size: 36px; }

  .contact {
    position: absolute; right: 22px; top: 34px;
    text-align: right; color: var(--ink-light);
  }
  .contact-name { color: var(--accent-red); font-weight: 700; font-size: 19px; white-space: nowrap; }
  .contact-role { font-size: 11px; margin-top: 2px; }
  .contact-address { font-size: 11px; line-height: 14px; margin-top: 16px; }
  .contact-lines { list-style: none; margin-top: 14px; font-size: 11px; line-height: 17px; }
  .contact-lines li { display: flex; justify-content: flex-end; align-items: center; gap: 6px; white-space: nowrap; }
  .contact-lines svg { width: 10px; height: 10px; fill: var(--accent-red); flex: none; }
</style>
</head>
<body>
<main class="stage">
  <section class="card card-back" aria-label="Card reverse">
    <div class="brand-lockup">
      <span class="brand-mark"></span>
      <span class="brand-name">Pharvelix</span>
    </div>
    <p class="tagline">Care Beyond Borders</p>
  </section>

  <section class="card card-front" aria-label="Card front">
    <svg class="front-panel" viewBox="0 0 500 286" aria-hidden="true">
      <polygon points="306,0 500,0 500,286 358,286" fill="var(--brand-blue)"/>
      <polygon points="298,0 303,0 355,286 350,286" fill="var(--accent-red)"/>
    </svg>
    <div class="brand-lockup">
      <span class="brand-mark"></span>
      <span class="brand-name">Pharvelix</span>
    </div>
    <div class="contact">
      <p class="contact-name">Rohan K. Tavde</p>
      <p class="contact-role">CEO</p>
      <p class="contact-address">12, Sunrise Nagar, Nashik<br>422005, India</p>
      <ul class="contact-lines">
        <li>+919800011223
          <svg viewBox="0 0 10 10"><path d="M2 0.5 L3.6 2.6 L2.8 3.6 C3.4 5 4.9 6.5 6.4 7.2 L7.4 6.4 L9.5 8 L8.4 9.5 C4.5 9.3 0.7 5.5 0.5 1.6 Z"/></svg>
        </li>
        <li>rtavde@pharvelix.com
          <svg viewBox="0 0 10 10"><path d="M0.5 2 H9.5 V8 H0.5 Z M1.2 2.6 L5 5.4 L8.8 2.6" stroke="var(--brand-blue)" stroke-width="0.8"/></svg>
        </li>
        <li>www.pharvelix.com
          <svg viewBox="0 0 10 10"><circle cx="5" cy="5" r="4.5"/><path d="M0.5 5 H9.5 M5 0.5 C2.5 3 2.5 7 5 9.5 M5 0.5 C7.5 3 7.5 7 5 9.5" stroke="var(--brand-blue)" stroke-width="0.7" fill="none"/></svg>
        </li>
      </ul>
    </div>
  </section>
</main>
</body>
</html>
```